Criação de Layout Web-Design para Decoração & Mobília
" Produzimos sofas, poltronas e puff de alta qualidade, com produção customizada para cada cliente. Atendemos clientes em todo território nacional, através de nossos representantes comerciais ou por meio eletrônico diretamente com a fabrica. Trabalhamos com as melhores materias primas do mercado e temos uma linha de tecidos importada que transformam os estofados em produtos exclusivos e de alta qualidade. "

```html
<!DOCTYPE html>
<html lang="pt-BR">
<head>
<meta charset="UTF-8">
<title>LUMA — Novidades</title>
<link href="https://fonts.googleapis.com/css2?family=Raleway:wght@300;400;500;600;700&display=swap" rel="stylesheet">
<style>
  :root{
    --header-bg:#1b1b1b;
    --header-text:#e8e8e8;
    --gold:#a88a5a;
    --gold-dark:#97794b;
    --page-bg:#ffffff;
    --sidebar-bg:#f3f3f3;
    --text:#3a3a3a;
    --muted:#8a8a8a;
    --photo-light:#eeeae4;
    --photo-mid:#d9cdb9;
  }
  *{box-sizing:border-box;margin:0;padding:0}
  html,body{width:1200px;height:1200px;overflow:hidden;background:var(--page-bg)}
  body{font-family:"Raleway",sans-serif;color:var(--text)}
  .site{width:1200px;height:1200px;display:flex;flex-direction:column}
  .site-header{height:130px;background:var(--header-bg);display:flex;align-items:center;padding:0 60px}
  .brand{font-size:40px;font-weight:600;letter-spacing:4px;color:var(--gold);display:flex;align-items:center;gap:12px}
  .brand-square{width:14px;height:14px;background:var(--gold)}
  .main-nav{margin-left:auto;display:flex;align-items:center;gap:30px}
  .main-nav a{color:var(--header-text);text-decoration:none;font-size:14px;font-weight:500;letter-spacing:1px;text-transform:uppercase}
  .main-nav a.is-active{color:var(--gold)}
  .nav-search{width:20px;height:20px}
  .site-body{flex:1;display:flex}
  .sidebar{width:230px;background:var(--sidebar-bg);padding:50px 0 0 60px}
  .sidebar-title{color:var(--gold);font-size:16px;font-weight:600;letter-spacing:1.5px;margin-bottom:22px}
  .category-list{list-style:none}
  .category-list li{font-size:14px;letter-spacing:1px;text-transform:uppercase;line-height:26px;color:var(--text)}
  .category-list li.is-current{font-weight:700}
  .news{flex:1;padding:50px 60px 0 40px}
  .news-title{color:var(--gold);font-size:22px;font-weight:600;letter-spacing:1.5px;margin-bottom:30px}
  .news-grid{display:grid;grid-template-columns:repeat(3,1fr);gap:34px}
  .news-card .news-photo{height:220px;background:linear-gradient(180deg,var(--photo-light),var(--photo-mid))}
  .news-card .news-photo.dark{background:linear-gradient(180deg,#f1f1f1,#cfcfcf 70%,#f1f1f1)}
  .card-title{margin-top:18px;font-size:14px;font-weight:600;text-transform:uppercase;letter-spacing:.5px}
  .card-text{margin-top:10px;font-size:12.5px;line-height:18px;color:var(--muted)}
  .card-date{margin-top:10px;font-size:12px;color:var(--muted)}
  .card-button{display:inline-block;margin-top:20px;background:var(--gold-dark);color:#fff;font-size:13px;font-weight:700;letter-spacing:1px;padding:12px 26px;text-transform:uppercase}
</style>
</head>
<body>
<div class="site">
  <header class="site-header">
    <div class="brand"><span class="brand-square"></span>LUMA</div>
    <nav class="main-nav">
      <a href="#">Home</a>
      <a href="#">Produtos</a>
      <a href="#" class="is-active">Novidades</a>
      <a href="#">Loja Virtual</a>
      <a href="#">Representantes</a>
      <a href="#">Fale Conosco</a>
      <svg class="nav-search" viewBox="0 0 20 20" aria-label="Buscar"><circle cx="8" cy="8" r="6" fill="none" stroke="#e8e8e8" stroke-width="2.2"/><line x1="12.5" y1="12.5" x2="18" y2="18" stroke="#e8e8e8" stroke-width="2.5" stroke-linecap="round"/></svg>
    </nav>
  </header>
  <div class="site-body">
    <aside class="sidebar">
      <h2 class="sidebar-title">CATEGORIAS</h2>
      <ul class="category-list">
        <li class="is-current">Todas</li>
        <li>Notícias</li>
        <li>Manutenção</li>
        <li>Limpeza</li>
        <li>Eventos</li>
        <li>Diversos</li>
        <li>Decoração</li>
      </ul>
    </aside>
    <main class="news">
      <h1 class="news-title">FIQUE POR DENTRO!</h1>
      <div class="news-grid">
        <article class="news-card">
          <div class="news-photo" role="img" aria-label="Foto de sofá bege em sala clara com luminárias"></div>
          <h3 class="card-title">Título do assunto/matéria</h3>
          <p class="card-text">A maciez do sofá de seção Helena está em suas dimensões generosas. Braços largos, assento profundo e encosto alto para o conforto da família.</p>
          <p class="card-date">21/02/2016</p>
          <a class="card-button" href="#">Saiba mais</a>
        </article>
        <article class="news-card">
          <div class="news-photo dark" role="img" aria-label="Foto de poltrona de couro preta"></div>
          <h3 class="card-title">Título do assunto/matéria</h3>
          <p class="card-text">A maciez do sofá de seção Helena está em suas dimensões generosas. Braços largos, assento profundo e encosto alto para o conforto da família.</p>
          <p class="card-date">21/02/2016</p>
          <a class="card-button" href="#">Saiba mais</a>
        </article>
        <article class="news-card">
          <div class="news-photo" role="img" aria-label="Foto de sofá bege com mesa lateral e luminárias"></div>
          <h3 class="card-title">Título do assunto/matéria</h3>
          <p class="card-text">A maciez do sofá de seção Helena está em suas dimensões generosas. Braços largos, assento profundo e encosto alto para o conforto da família.</p>
          <p class="card-date">21/02/2016</p>
          <a class="card-button" href="#">Saiba mais</a>
        </article>
      </div>
    </main>
  </div>
</div>
</body>
</html>
```